business card with logo Velmora Nails & Spa 2816 SW Quillan Ave Portland OR 97384

Would like to have a business card with our logo.
like bottle of polish with our logo or letter V on it
want something that first glance would let you know that it is a nail salon.
like the hands with polish bottle dripping.
like black or White back ground

Velmora Nails & Spa
(The Velvet Retreat)
2816 SW Quillan Ave
Portland, OR 97384
Call or Text: 1-503-555-0148
www.VelmoraNailsnSpa.example
Open 7 days a week.
After 7:00 PM is by appointment only.
Closed only on Thanksgiving & Christmas.

Target Market(s)

20%Man and 80%Woman 13-70

Industry/Entity Type

Business

Contact Information for Business Card

Elegant with Logo-Business name- address-phone-open days. closed day.

Font styles to use
Decorative
Script

Colors
000000

Requirements
Must have
• Logo and place for Technician Name
• Velmora Nails & Spa
• (The Velvet Retreat)
• 2816 SW Quillan Ave
• Portland, OR 97384
• Call or Text: 1-503-555-0148
• Open 7 days a week
• Closed only on Thanksgiving & Christmas.
• We accepted all major credit cards but prefer cash. Thank you
Nice to have
• Nail polish bottle with our Logo or letter V
Should not have
• too colorful

```html
<!DOCTYPE html>
<html lang="en">
<head>
<meta charset="utf-8">
<title>Velmora Nails &amp; Spa – Business Card</title>
<link href="https://fonts.googleapis.com/css2?family=Open+Sans:wght@400;600&display=swap" rel="stylesheet">
<style>
  :root {
    --stage: #e9e6e1;
    --card-white: #ffffff;
    --card-black: #141414;
    --ink: #2a2a2a;
    --ink-soft: #6a6a6a;
    --ink-light: #f2f2f2;
    --ink-light-soft: #b8b8b8;
    --accent-green: #c6e23a;
    --polish-red: #d42a22;
    --skin: #f1cdb9;
    --icon-red: #e0463c;
    --chip-white: #f4f4f4;
    --chip-blue: #2f7fc4;
    --chip-sky: #4fb0e0;
    --chip-orange: #ef8a2a;
  }
  * { box-sizing: border-box; margin: 0; padding: 0; }
  html, body {
    width: 771px; height: 1200px; overflow: hidden;
    background: var(--stage);
    font-family: "Open Sans", Arial, sans-serif;
  }
  .canvas { position: relative; width: 771px; height: 1200px; }
  .card {
    position: absolute; left: 220px; width: 330px; height: 578px;
    border-radius: 6px; overflow: hidden;
    box-shadow: 0 6px 18px rgba(0,0,0,.18);
  }
  .card--front { top: 11px; background: var(--card-white); color: var(--ink); }
  .card--back { top: 611px; background: linear-gradient(160deg, #262626 0%, var(--card-black) 55%, #0a0a0a 100%); color: var(--ink-light); }

  .polish-photo {
    position: absolute; right: 0; top: 24px; width: 140px; height: 300px;
    border-radius: 8px 0 0 8px;
    background: linear-gradient(180deg, var(--skin) 0%, #f3dccf 30%, #f6e2e0 48%, #e6857e 70%, var(--polish-red) 100%);
  }

  .logo { position: absolute; font-weight: 600; }
  .logo__name { display: block; font-size: 36px; line-height: 1; letter-spacing: .5px; }
  .logo__tag { display: block; font-size: 14px; margin-top: 5px; letter-spacing: .5px; }
  .logo__subtitle { display: block; font-size: 12px; font-weight: 400; margin-top: 3px; }
  .card--front .logo { left: 26px; top: 132px; color: var(--ink); }
  .card--front .logo__subtitle { color: var(--ink-soft); }
  .card--back .logo { left: 0; right: 0; top: 92px; text-align: center; color: var(--ink-light); }
  .card--back .logo__name { font-size: 40px; }
  .card--back .logo__subtitle { color: var(--ink-light-soft); }

  .technician { position: absolute; left: 26px; right: 26px; top: 352px; font-size: 12px; color: var(--ink-soft); display: flex; align-items: flex-end; gap: 8px; }
  .technician__line { flex: 1; border-bottom: 1px solid #9a9a9a; height: 14px; }

  .contact { position: absolute; left: 26px; bottom: 58px; list-style: none; font-size: 13.5px; line-height: 1.45; }
  .contact li { display: flex; align-items: flex-start; gap: 8px; margin-top: 4px; }
  .contact svg { flex: none; margin-top: 3px; }

  .hours { position: absolute; left: 0; right: 0; top: 290px; text-align: center; font-size: 14px; line-height: 1.6; }
  .cards-note { position: absolute; left: 0; right: 0; top: 390px; text-align: center; font-size: 14px; color: var(--accent-green); }
  .payment-row { position: absolute; left: 20px; right: 20px; top: 428px; display: flex; justify-content: space-between; }
  .payment-chip {
    width: 66px; height: 42px; border-radius: 5px;
    display: flex; align-items: center; justify-content: center;
    font-size: 10px; font-weight: 600; color: var(--ink);
    box-shadow: 0 2px 6px rgba(0,0,0,.5);
  }
  .payment-chip--white { background: var(--chip-white); }
  .payment-chip--blue { background: var(--chip-blue); color: #fff; }
  .payment-chip--sky { background: var(--chip-sky); color: #fff; }
  .payment-chip--orange { background: linear-gradient(180deg, var(--chip-white) 60%, var(--chip-orange) 60%); }
  .cash-note { position: absolute; left: 0; right: 0; top: 496px; text-align: center; font-size: 13px; color: var(--ink-light-soft); }
</style>
</head>
<body>
<main class="canvas">

  <section class="card card--front" aria-label="Business card front">
    <div class="polish-photo" role="img" aria-label="Hand with red nails holding a brush dripping red polish into a bottle"></div>
    <div class="logo">
      <span class="logo__name">Velmora</span>
      <span class="logo__tag">Nails n Spa</span>
      <span class="logo__subtitle">(The Velvet Retreat)</span>
    </div>
    <div class="technician"><span>Technician:</span><span class="technician__line"></span></div>
    <ul class="contact">
      <li>
        <svg width="10" height="13" viewBox="0 0 10 13"><path d="M5 0a4.5 4.5 0 0 0-4.5 4.5C.5 8 5 13 5 13s4.5-5 4.5-8.5A4.5 4.5 0 0 0 5 0z" fill="var(--icon-red)"/><circle cx="5" cy="4.5" r="1.6" fill="#fff"/></svg>
        <span>2816 SW Quillan Ave<br>Portland, OR 97384</span>
      </li>
      <li>
        <svg width="10" height="13" viewBox="0 0 10 13"><rect x="1" y=".5" width="8" height="12" rx="1.5" fill="none" stroke="var(--icon-red)" stroke-width="1.2"/><circle cx="5" cy="10.3" r=".8" fill="var(--icon-red)"/></svg>
        <span>1-503-555-0148(Call or Text)</span>
      </li>
      <li>
        <svg width="12" height="12" viewBox="0 0 12 12"><circle cx="6" cy="6" r="5.3" fill="none" stroke="var(--icon-red)" stroke-width="1.1"/><ellipse cx="6" cy="6" rx="2.3" ry="5.3" fill="none" stroke="var(--icon-red)" stroke-width="1"/><path d="M.7 6h10.6" stroke="var(--icon-red)" stroke-width="1"/></svg>
        <span>www.VelmoraNailsnSpa.example</span>
      </li>
    </ul>
  </section>

  <section class="card card--back" aria-label="Business card back">
    <div class="logo">
      <span class="logo__name">Velmora</span>
      <span class="logo__tag">Nails n Spa</span>
      <span class="logo__subtitle">(The Velvet Retreat)</span>
    </div>
    <p class="hours">Open 7 days a week.<br>After 7:00 PM is by appointment only.<br>Closed only on Thanksgiving &amp; Christmas</p>
    <p class="cards-note">We Accept All major credit cards:</p>
    <div class="payment-row">
      <span class="payment-chip payment-chip--white">Crestpay</span>
      <span class="payment-chip payment-chip--blue">Meridian</span>
      <span class="payment-chip payment-chip--sky">Anchor Exp</span>
      <span class="payment-chip payment-chip--orange">Northway</span>
    </div>
    <p class="cash-note">But prefer cash. Thank you</p>
  </section>

</main>
</body>
</html>
```